Label design: italian artisan honey (to allow tradition look attractive!)

Founded in 1973, this specialized business in artisan honey, is based in Emilia-Romagna. It accounts for 10 apiary locations, honey is organic, whereas the equipment to rise, and control bees are all hand made.
The symbol, (you will find the logo corvasti.ai) is a hexagonal hunting house built in the 17th century. The structure is protected by fine-arts and retains its stucco works and frescoes depicting mythological scenes. The place is located in the hills, next to a hunting area, and surrounded by our ecological farm.

Please find the foto of the label that has been used for over 30 years and also the Italian Beekeeper association label that is placed on all the vases.

Target Market(s)

Local gastronomic shop owners, where local consumers are both young and mature families, well-read, connaisseurs, curious, with strong social ties also with nature.

Font styles to use
Serif
Sans Serif

Requirements
Must have
• We have a glass jar already with specific dimensions.
The lid finishing is metallic finishing, in copper color.
We need the label to have the by-law necessary information of the product on it:
Honey type, producer name, weight, best by date, origin.
The lid measures 6 cm in diameter, and has a border of about 0.5 cm.
The visible part of the glass jar is 3 cm high.
You can get inspired by the type of package we want to use: (in light wood or carton board as materials as in the 2 examples we attach is actually like a matchbox).
We also attached an illustrator file with the logo shape, colors to be adapted to your design, consider the "grey color" and the "metallic finishing" on the corner, as shown in the file ref_glimfold_3.
Nice to have
• The _pack_1 and _pack_3 files are mood ideas for the box, to provide you inspiration for the label.
The color palette is provided by two files :
ref_glimfold_3 ;
color_palette_corvasti.
The font reference is provided by two files :
Typeface ;
ref_typeface.

```html
<!DOCTYPE html>
<html lang="it">
<head>
<meta charset="utf-8">
<title>Corvasti Miele – etichette</title>
<link rel="stylesheet" href="https://fonts.googleapis.com/css2?family=Jost:wght@300;400;600;700&display=swap">
<style>
  :root {
    --paper: #ffffff;
    --honey-orange: #f4914a;
    --honey-orange-light: #f6a263;
    --bark: #5b504d;
    --bark-light: #6a5f5b;
    --ink: #4a403d;
    --cream: #ffffff;
    --shadow: rgba(0, 0, 0, 0.28);
  }
  * { margin: 0; padding: 0; box-sizing: border-box; }
  html, body {
    width: 995px; height: 1200px; overflow: hidden;
    background: var(--paper);
    font-family: "Jost", sans-serif;
  }
  .sheet { position: relative; width: 995px; height: 1200px; }

  /* Lid label */
  .lid-label {
    position: absolute; left: 295px; top: 218px;
    width: 404px; height: 404px; border-radius: 50%;
    background: radial-gradient(circle at 50% 50%, var(--honey-orange-light), var(--honey-orange) 70%);
    box-shadow: 0 10px 22px var(--shadow);
  }
  .brand-square {
    position: absolute; left: 50%; top: 54px; transform: translateX(-50%);
    width: 60px; height: 60px; background: var(--cream);
  }
  .lid-brand {
    position: absolute; left: 0; right: 0; top: 136px; text-align: center;
    font-weight: 300; font-size: 34px; letter-spacing: 1px; color: var(--ink);
  }
  .lid-sub {
    position: absolute; left: 0; right: 0; top: 182px; text-align: center;
    font-weight: 700; font-size: 15px; letter-spacing: 5px; color: var(--cream);
  }
  .lid-variety {
    position: absolute; left: 0; right: 0; top: 262px; text-align: center;
    font-weight: 600; font-size: 29px; color: var(--ink);
  }

  /* Neck strip */
  .neck-strip {
    position: absolute; left: 419px; top: 614px; width: 156px; height: 212px;
    background: var(--bark);
    box-shadow: 0 6px 14px var(--shadow);
  }
  .neck-strip .brand-square {
    top: 28px; width: 52px; height: 52px;
  }
  .neck-brand {
    position: absolute; left: 0; right: 0; top: 124px; text-align: center;
    font-weight: 300; font-size: 23px; color: var(--cream);
  }

  /* Body band */
  .body-band {
    position: absolute; left: 30px; top: 826px; width: 936px; height: 156px;
    display: flex; box-shadow: 0 10px 20px var(--shadow);
  }
  .band-side {
    width: 194px; height: 100%; background: var(--bark);
    position: relative; color: var(--cream);
  }
  .band-front {
    flex: 1; height: 100%; position: relative; text-align: center; color: var(--cream);
  }
  .pattern-fill {
    position: absolute; inset: 0;
  }
  .band-front .pattern-fill { background: linear-gradient(90deg, var(--honey-orange), var(--honey-orange-light) 50%, var(--honey-orange)); }
  .band-side .pattern-fill { background: linear-gradient(90deg, var(--bark), var(--bark-light) 50%, var(--bark)); }
  .front-title {
    position: absolute; left: 0; right: 0; top: 14px;
    font-weight: 600; font-size: 32px; line-height: 1; letter-spacing: -0.5px;
  }
  .front-origin {
    position: absolute; left: 0; right: 0; top: 52px;
    font-weight: 300; font-size: 36px; line-height: 1;
  }
  .front-made {
    position: absolute; left: 0; right: 0; top: 120px;
    font-weight: 300; font-size: 17px; line-height: 1;
  }
  .best-before {
    position: absolute; left: 97px; top: 78px;
    transform: translate(-50%, -50%) rotate(90deg);
    text-align: center; font-weight: 300; font-size: 16px; line-height: 1.2;
    white-space: nowrap;
  }
  .batch-info {
    position: absolute; left: 26px; top: 48px;
    font-weight: 300; font-size: 22px; line-height: 36px;
  }
</style>
</head>
<body>
<main class="sheet">

  <section class="lid-label" aria-label="Etichetta coperchio">
    <div class="pattern-fill" role="img" aria-label="Motivo decorativo a sole tribale in arancio tono su tono" style="border-radius:50%"></div>
    <div class="brand-square"></div>
    <div class="lid-brand">CORVASTI</div>
    <div class="lid-sub">MIELE</div>
    <div class="lid-variety">MIELE DI ACACIA</div>
  </section>

  <section class="neck-strip" aria-label="Sigillo">
    <div class="pattern-fill" role="img" aria-label="Motivo decorativo tribale in grigio tono su tono" style="background:linear-gradient(var(--bark),var(--bark-light))"></div>
    <div class="brand-square"></div>
    <div class="neck-brand">CORVASTI</div>
  </section>

  <section class="body-band" aria-label="Fascia vasetto">
    <div class="band-side">
      <div class="pattern-fill" role="img" aria-label="Motivo decorativo tribale in grigio"></div>
      <div class="best-before">Consumare<br>Preferibilmente<br>entro</div>
    </div>
    <div class="band-front">
      <div class="pattern-fill" role="img" aria-label="Motivo decorativo tribale in arancio tono su tono"></div>
      <div class="front-title">MIELE</div>
      <div class="front-origin">PIACENTINO</div>
      <div class="front-made">PRODOTTO IN ITALIA</div>
    </div>
    <div class="band-side">
      <div class="pattern-fill" role="img" aria-label="Motivo decorativo tribale in grigio"></div>
      <div class="batch-info">Lotto:<br>Peso:</div>
    </div>
  </section>

</main>
</body>
</html>
```